New years sale mail box drop flyer

We are Vortel Fitness Ashgrove, a 24/7 gym located in a quiet suburb of Brisbane. We are a friendly, affordable and convenient facility which offers our members a clean and air-conditioned gym with state of the art and easy to use equipment, showers and toilets. We offer a variety of flexible membership options as well as offering one on one and small group (2-4) personal training sessions and large group sessions. Our qualified staff are friendly, professional and always approachable. We try to put a strong emphasis on 'lifestyle changes' in order to reach goals rather than the quick fix fads. Our current members enjoy the quiet and intimidation free environment our gym provides.
Fitness

```html
<!DOCTYPE html>
<html lang="en">
<head>
<meta charset="utf-8">
<title>Vortel Fitness Ashgrove – Double Sided Flyer</title>
<link href="https://fonts.googleapis.com/css2?family=Open+Sans:wght@300;700&family=Roboto+Condensed:wght@400&family=Urbanist:wght@400;700;800&display=swap" rel="stylesheet">
<style>
  :root {
    --orange: #f58529;
    --orange-deep: #f07c1f;
    --charcoal: #58585a;
    --white: #ffffff;
    --page: #ffffff;
  }
  * { margin: 0; padding: 0; box-sizing: border-box; }
  html, body { width: 1200px; height: 927px; overflow: hidden; background: var(--page); }
  .sheet { position: relative; width: 1200px; height: 927px; }

  .flyer { position: absolute; top: 180px; width: 464px; height: 654px; overflow: hidden; }
  .flyer--front { left: 78px; background: var(--orange); }
  .flyer--back { left: 658px; background: var(--charcoal); }

  /* Front */
  .front-brand { position: absolute; left: 210px; top: 30px; width: 232px; text-align: center; color: var(--white); }
  .front-brand__name { font-family: "Urbanist", sans-serif; font-weight: 800; font-size: 29px; line-height: 1; }
  .front-brand__place { font-family: "Urbanist", sans-serif; font-weight: 700; font-size: 16px; letter-spacing: 12px; margin-top: 22px; margin-right: -12px; }

  .vertical { position: absolute; transform-origin: left top; transform: rotate(-90deg);
    font-family: "Open Sans", sans-serif; color: var(--white); white-space: nowrap; line-height: 1; }
  .vertical--lifestyle { left: 18px; top: 616px; font-size: 162px; font-weight: 700; letter-spacing: -10px; }
  .vertical--change { left: 162px; top: 614px; font-size: 110px; font-weight: 300; letter-spacing: -1px; }

  /* Back */
  .back-shapes { position: absolute; inset: 0; }
  .back-brand { position: absolute; left: 80px; top: 26px; width: 370px; text-align: center; color: var(--white); }
  .back-brand__name { font-family: "Urbanist", sans-serif; font-weight: 800; font-size: 42px; line-height: 1; }
  .back-brand__place { font-family: "Urbanist", sans-serif; font-weight: 700; font-size: 24px; letter-spacing: 19px; margin-right: -19px; margin-top: 38px; line-height: 1; }
  .back-tagline { position: absolute; left: 40px; right: 0; top: 150px; text-align: center; color: var(--white);
    font-family: "Urbanist", sans-serif; font-weight: 700; font-size: 20px; line-height: 27px; }

  .features { list-style: none; position: absolute; left: 0; right: 0; top: 0; }
  .features li { position: absolute; left: 12px; right: 0; height: 29px; line-height: 29px; text-align: center;
    font-family: "Roboto Condensed", sans-serif; font-size: 19px; color: var(--white); letter-spacing: 0.4px; }

  .cta { position: absolute; left: 60px; right: 18px; top: 496px; font-family: "Urbanist", sans-serif; color: var(--orange); line-height: 1; }
  .cta__line { display: flex; align-items: baseline; justify-content: flex-end; gap: 12px; white-space: nowrap; }
  .cta__line + .cta__line { margin-top: 12px; }
  .cta__bold { font-weight: 800; font-size: 58px; }
  .cta__light { font-weight: 400; font-size: 40px; letter-spacing: 1px; }
  .cta__light--big { font-size: 50px; }
  .cta__bold--small { font-size: 34px; }

  .contact { position: absolute; left: 10px; right: 8px; bottom: 0; height: 38px; display: flex; align-items: center; justify-content: space-between;
    font-family: "Urbanist", sans-serif; font-weight: 800; font-size: 13.5px; color: var(--white); }
  .contact__item { display: flex; align-items: center; gap: 5px; }
  .contact__item svg { width: 15px; height: 15px; flex: none; }
</style>
</head>
<body>
<div class="sheet">

  <section class="flyer flyer--front" aria-label="Flyer front">
    <div class="front-brand">
      <div class="front-brand__name">Vortel Fitness</div>
      <div class="front-brand__place">ASHGROVE</div>
    </div>
    <div class="vertical vertical--lifestyle">lifestyle</div>
    <div class="vertical vertical--change">change</div>
  </section>

  <section class="flyer flyer--back" aria-label="Flyer back">
    <svg class="back-shapes" width="464" height="654" viewBox="0 0 464 654">
      <defs>
        <linearGradient id="headerFill" x1="0" y1="0" x2="0" y2="1">
          <stop offset="0" stop-color="#f58529"/>
          <stop offset="0.85" stop-color="#f58529"/>
          <stop offset="1" stop-color="#f79a52"/>
        </linearGradient>
        <linearGradient id="band1" x1="0" y1="0" x2="0" y2="1"><stop offset="0" stop-color="#f6a463"/><stop offset="1" stop-color="#f8b27a"/></linearGradient>
        <linearGradient id="band2" x1="0" y1="0" x2="0" y2="1"><stop offset="0" stop-color="#f8ba88"/><stop offset="1" stop-color="#f9c79f"/></linearGradient>
        <linearGradient id="band3" x1="0" y1="0" x2="0" y2="1"><stop offset="0" stop-color="#fad0ae"/><stop offset="1" stop-color="#fde6d4"/></linearGradient>
        <linearGradient id="band4" x1="0" y1="0" x2="0" y2="1"><stop offset="0" stop-color="#fde3cf"/><stop offset="1" stop-color="#ffffff"/></linearGradient>
      </defs>
      <path d="M90,0 H464 V224 H21 C25,140 48,55 90,0 Z" fill="url(#headerFill)"/>
      <rect x="16" y="253" width="448" height="29" fill="url(#band1)"/>
      <rect x="14" y="311" width="450" height="30" fill="url(#band2)"/>
      <rect x="16" y="370" width="448" height="28" fill="url(#band3)"/>
      <rect x="21" y="427" width="443" height="30" fill="url(#band4)"/>
      <path d="M29,486 H464 V616 H72 C52,580 37,535 29,486 Z" fill="#ffffff"/>
    </svg>

    <div class="back-brand">
      <div class="back-brand__name">Vortel Fitness</div>
      <div class="back-brand__place">ASHGROVE</div>
    </div>
    <p class="back-tagline">Our qualified staff are friendly,<br>professional and always approachable.</p>

    <ul class="features">
      <li style="top:224px">CLEAN AND AIR-CONDITIONED GYM</li>
      <li style="top:282px">EASY TO USE EQUIPMENT</li>
      <li style="top:341px">VARIETY OF FLEXIBLE MEMBERSHIP OPTIONS</li>
      <li style="top:398px">PERSONAL TRAINING SESSIONS</li>
      <li style="top:457px">LARGE GROUP SESSIONS</li>
    </ul>

    <div class="cta">
      <div class="cta__line"><span class="cta__bold">CHANGE</span><span class="cta__light">YOUR</span></div>
      <div class="cta__line"><span class="cta__light cta__light--big">LIFESTYLE</span><span class="cta__bold cta__bold--small">TODAY!</span></div>
    </div>

    <div class="contact">
      <span class="contact__item">
        <svg viewBox="0 0 16 16"><circle cx="8" cy="8" r="8" fill="#f58529"/><path d="M3.5,8.2 L8,4.2 L12.5,8.2 H11 V12 H9 V9.5 H7 V12 H5 V8.2 Z" fill="#fff"/></svg>
        24 LINDEN ROAD
      </span>
      <span class="contact__item">
        <svg viewBox="0 0 16 16"><circle cx="8" cy="8" r="8" fill="#f58529"/><path d="M5,4 L6.8,4 L7.4,6.2 L6.4,7 C7,8.3 7.7,9 9,9.6 L9.8,8.6 L12,9.2 L12,11 C8,11.3 4.7,8 5,4 Z" fill="#fff"/></svg>
        07 3000 0000
      </span>
      <span class="contact__item">
        <svg viewBox="0 0 16 16"><rect x="0" y="2" width="16" height="12" rx="2" fill="#f58529"/><path d="M2.5,4.5 L8,8.5 L13.5,4.5" stroke="#fff" stroke-width="1.4" fill="none"/></svg>
        hello@vortelfit.com
      </span>
    </div>
  </section>

</div>
</body>
</html>
```